Venlox - Property Management Company Listings - PSD / uncoded only

Our site simply connects property owners with property managers. I’m asking you to create 2 pages, 1 homepage and 1 page that lists of property management companies. Build with Responsive Design in mind. PSD/uncoded files only. Help us create a great site!
Example competitor sites:
http://www.everyestatehelp.example/
http://www.tendyourlots.example/
Inspired by these sites:
http://www.quorvik.example/
http://www.bespokely.example/
http://www.coinwire.example/
https://www.tripboard.example/
I've attached the logo as well as 2 picture files that you can consider using.
• Venlox Logo Colors: Yellow: HTML code: #FBC30A, RGB code: R: 251 G: 195 B: 10 Grey: HTML code: #4E4C4D, RGB code: R: 78 G: 76 B: 77
• The picture files are optional.
o One picture is of houses and neighborhood.
o The other is of a professional woman on the phone. Please do not use the professional woman as a large primary image. You can use the professional woman photo as a smaller photo and not the main photo.
• Please bring your own pictures and graphics too. Don't feel like you need to use mine.
Thank you!

```html
<!DOCTYPE html>
<html lang="en">
<head>
<meta charset="utf-8">
<title>Venlox – Property Management Companies</title>
<link href="https://fonts.googleapis.com/css2?family=Montserrat:wght@400;600;700&family=Open+Sans:wght@400;600&display=swap" rel="stylesheet">
<style>
  :root {
    --brand-yellow: #fbc30a;
    --brand-grey: #4e4c4d;
    --page-bg: #f4f4f4;
    --white: #ffffff;
    --ink: #3a3a3a;
    --muted: #9a9a9a;
    --link-blue: #3a8fd8;
    --btn-blue: #2c8ee0;
    --dark-band: #1e2022;
    --footer-bg: #262626;
    --field-border: #cfcfcf;
  }
  * { box-sizing: border-box; margin: 0; padding: 0; }
  html, body { width: 692px; height: 1200px; overflow: hidden; }
  body {
    position: relative;
    background: var(--page-bg);
    font-family: "Open Sans", Arial, sans-serif;
    color: var(--ink);
  }

  /* Header */
  .site-header {
    position: absolute; left: 0; top: 0; width: 692px; height: 37px;
    background: linear-gradient(#ffffff, #ececec);
    border-bottom: 1px solid #d8d8d8;
  }
  .brand { position: absolute; left: 136px; top: 7px; display: flex; align-items: center; gap: 5px; }
  .brand-mark { width: 10px; height: 10px; background: var(--brand-yellow); }
  .brand-name {
    font-family: "Montserrat", Arial, sans-serif; font-weight: 700;
    font-size: 21px; color: var(--brand-grey); line-height: 24px;
  }
  .nav-link {
    position: absolute; top: 11px; height: 14px; line-height: 14px;
    font-size: 5.6px; color: #666; text-decoration: none; white-space: nowrap;
  }
  .nav-link.is-active { left: 391px; width: 32px; text-align: center; background: #dedede; border-radius: 7px; }
  .nav-link.is-plain { left: 430px; }
  .btn-signin {
    position: absolute; left: 506px; top: 11px; width: 46px; height: 16px;
    background: var(--btn-blue); color: var(--white); border-radius: 2px;
    font-family: "Montserrat", Arial, sans-serif; font-weight: 700; font-size: 6px;
    display: flex; align-items: center; justify-content: center;
  }

  /* Hero */
  .hero-photo {
    position: absolute; left: 0; top: 37px; width: 692px; height: 255px;
    background: radial-gradient(ellipse at 50% 40%, #4b5a52 0%, #2d3a31 55%, #1a231c 100%);
  }
  .hero-title {
    position: absolute; left: 0; top: 103px; width: 692px; text-align: center;
    font-family: "Montserrat", Arial, sans-serif; font-weight: 700;
    font-size: 17px; line-height: 23px; color: var(--white);
  }
  .hero-points { position: absolute; top: 164px; left: 0; width: 692px; font-size: 7px; color: var(--white); font-weight: 600; }
  .hero-points span { position: absolute; white-space: nowrap; }
  .hero-points span::before {
    content: ""; display: inline-block; width: 4px; height: 4px; border-radius: 50%;
    background: var(--brand-yellow); margin-right: 7px; vertical-align: middle;
  }
  .search-panel {
    position: absolute; left: 138px; top: 199px; width: 414px; height: 45px;
    background: var(--white);
  }
  .field {
    position: absolute; top: 13px; height: 20px; border: 1px solid var(--field-border);
    font-size: 5px; color: #888; padding-left: 6px; display: flex; align-items: center;
    background: #fafafa;
  }
  .field.is-focus { border-color: #7fb2e0; background: #fff; }
  .field .caret { position: absolute; right: 6px; top: 8px; width: 0; height: 0;
    border-left: 2.5px solid transparent; border-right: 2.5px solid transparent; border-top: 3px solid #666; }
  .btn-search {
    position: absolute; left: 316px; top: 13px; width: 89px; height: 19px;
    background: linear-gradient(#fcc91e, #f1b300); border-radius: 2px;
    color: var(--white); font-size: 8.5px; font-weight: 600;
    display: flex; align-items: center; justify-content: center; gap: 6px;
  }

  /* Services */
  .service { position: absolute; top: 306px; width: 96px; }
  .service-photo {
    width: 96px; height: 73px; border: 3px solid var(--white);
    box-shadow: 0 0 0 1px #d4d4d4;
  }
  .service-title { margin-top: 9px; font-family: "Montserrat", Arial, sans-serif; font-weight: 400; font-size: 7.5px; color: #444; white-space: nowrap; }
  .service-text { margin-top: 6px; padding-left: 2px; font-size: 6px; line-height: 9px; color: var(--muted); }
  .read-more { display: block; margin-top: 5px; padding-left: 2px; font-size: 5px; color: var(--link-blue); font-weight: 600; }

  /* Project list */
  .projects-band {
    position: absolute; left: 0; top: 448px; width: 692px; height: 270px;
    background: linear-gradient(#15181b 0%, #23272a 55%, #1b1d18 100%);
  }
  .section-kicker { position: absolute; left: 0; width: 692px; text-align: center; font-size: 6px; color: #888; }
  .projects-title {
    position: absolute; left: 0; top: 480px; width: 692px; text-align: center;
    font-family: "Montserrat", Arial, sans-serif; font-weight: 700; font-size: 9.5px; color: var(--brand-yellow);
  }
  .title-rule { position: absolute; height: 1px; background: var(--white); }
  .project-circle {
    position: absolute; left: 265px; top: 518px; width: 162px; height: 162px; border-radius: 50%;
    overflow: hidden; background: linear-gradient(#8a8f95 0%, #5d6268 45%, #4c5a44 100%);
  }
  .project-caption {
    position: absolute; left: 0; top: 124px; width: 162px; height: 38px;
    background: rgba(40,40,40,0.85); text-align: center;
  }
  .project-caption .name { margin-top: 4px; font-size: 7.5px; color: var(--white); font-family: "Montserrat", Arial, sans-serif; }
  .project-caption .rule { width: 30px; height: 1px; background: var(--brand-yellow); margin: 2px auto 2px; }
  .project-caption .sub { font-size: 5px; color: #aaa; }
  .arrow-btn { position: absolute; top: 591px; width: 30px; height: 30px; }

  /* Featured */
  .featured-title { position: absolute; left: 136px; top: 744px; font-family: "Montserrat", Arial, sans-serif; font-weight: 400; font-size: 10px; color: #222; }
  .featured-sub { position: absolute; left: 136px; top: 757px; font-size: 5px; color: #777; }
  .featured-rule { position: absolute; left: 136px; top: 766px; width: 57px; height: 1px; background: #d8b66a; }
  .tile { position: absolute; width: 132px; height: 87px; }
  .tile.is-hover { background: var(--brand-yellow); display: flex; align-items: center; justify-content: center; }

  /* Testimonial */
  .avatar { position: absolute; left: 323px; top: 1007px; width: 46px; height: 46px; border-radius: 50%;
    background: radial-gradient(circle at 50% 45%, #c7a58f, #6b4b3c 70%, #e8e8e8 72%); }
  .quote-name { position: absolute; left: 0; top: 1062px; width: 692px; text-align: center; font-size: 7px; color: #c99a12; }
  .quote-lead { position: absolute; left: 0; top: 1074px; width: 692px; text-align: center; font-size: 5px; color: #444; }
  .quote-body { position: absolute; left: 163px; top: 1090px; width: 366px; text-align: center; font-size: 4.6px; line-height: 8px; color: #aaa; }
  .quote-mark { position: absolute; font-family: Georgia, serif; font-weight: 700; font-size: 44px; color: #d6d6d6; line-height: 1; }

  /* Footer */
  .site-footer { position: absolute; left: 0; top: 1178px; width: 692px; height: 22px; background: var(--footer-bg); }
  .copyright { position: absolute; left: 136px; top: 7px; font-size: 4.8px; color: #ddd; }
  .social { position: absolute; left: 466px; top: 5px; display: flex; align-items: center; gap: 5px; font-size: 6px; color: #ccc; }
  .social-square { width: 12px; height: 12px; background: #5d6b80; border-radius: 1px; }
</style>
</head>
<body>

<header class="site-header">
  <div class="brand"><span class="brand-mark"></span><span class="brand-name">Venlox</span></div>
  <nav>
    <a class="nav-link is-active">Home</a>
    <a class="nav-link is-plain">Property Management</a>
  </nav>
  <div class="btn-signin">SIGN IN</div>
</header>

<div class="hero-photo" role="img" aria-label="Aerial photo of a waterfront residential neighbourhood at dusk"></div>
<h1 class="hero-title">WELCOME TO THE VENLOX PROPERTY<br>MANAGEMENT COMPANIES</h1>
<div class="hero-points">
  <span style="left:186px">Insurance Chears</span>
  <span style="left:288px">Money Ordrs</span>
  <span style="left:368px">Safe Deposit</span>
  <span style="left:450px">Trust Fund</span>
</div>

<form class="search-panel">
  <div class="field is-focus" style="left:9px;width:102px">Select Property Type</div>
  <div class="field" style="left:117px;width:102px">Property Zip</div>
  <div class="field" style="left:225px;width:85px">State<span class="caret"></span></div>
  <div class="btn-search">
    <svg width="8" height="8" viewBox="0 0 10 10"><circle cx="6" cy="4" r="3" fill="none" stroke="#fff" stroke-width="1.6"/><line x1="4" y1="6" x2="1" y2="9" stroke="#fff" stroke-width="1.8"/></svg>
    Search
  </div>
</form>

<section>
  <article class="service" style="left:137px">
    <div class="service-photo" role="img" aria-label="Smiling agent holding papers in front of a house" style="background:linear-gradient(135deg,#7a9bb8,#5c7da0 55%,#6f9a4e)"></div>
    <h3 class="service-title">Sed ut Perspiciatis</h3>
    <p class="service-text">Lorem ipsum dolor sit amet, consectetur adipisicing.</p>
    <a class="read-more">Read More ...</a>
  </article>
  <article class="service" style="left:244px">
    <div class="service-photo" role="img" aria-label="Hands holding a small grass-covered house" style="background:linear-gradient(135deg,#2e2e2e,#6e8a3a 50%,#8bb04a)"></div>
    <h3 class="service-title">Sed ut Perspiciatis</h3>
    <p class="service-text">Lorem ipsum dolor sit amet, consectetur adipisicing.</p>
    <a class="read-more">Read More ...</a>
  </article>
  <article class="service" style="left:351px">
    <div class="service-photo" role="img" aria-label="Businessman presenting a model house on a tray" style="background:linear-gradient(135deg,#3d4a5a,#8b98a8 55%,#c9ced4)"></div>
    <h3 class="service-title">Sed ut Perspiciatis</h3>
    <p class="service-text">Lorem ipsum dolor sit amet, consectetur adipisicing.</p>
    <a class="read-more">Read More ...</a>
  </article>
  <article class="service" style="left:458px">
    <div class="service-photo" role="img" aria-label="Hand handing over house keys with a small house keyring" style="background:linear-gradient(135deg,#3a3f46,#9da3aa 55%,#d8d8d8)"></div>
    <h3 class="service-title">Sed ut Perspiciatis</h3>
    <p class="service-text">Lorem ipsum dolor sit amet, consectetur adipisicing.</p>
    <a class="read-more" style="margin-top:9px">Read More ...</a>
  </article>
</section>

<div class="projects-band" role="img" aria-label="Dark evening sky over open fields"></div>
<p class="section-kicker" style="top:471px">Lorem ipsum</p>
<h2 class="projects-title">OUR PROJECT LIST</h2>
<div class="title-rule" style="left:337px;top:494px;width:18px"></div>
<div class="project-circle">
  <div role="img" aria-label="Two-storey grey house with a car in the driveway" style="position:absolute;inset:0"></div>
  <div class="project-caption">
    <p class="name">Dolor Sit Amet</p>
    <div class="rule"></div>
    <p class="sub">consectetur adipiscing</p>
  </div>
</div>
<svg class="arrow-btn" style="left:171px" viewBox="0 0 30 30"><circle cx="15" cy="15" r="15" fill="#e7b000"/><circle cx="15" cy="15" r="12" fill="#f6c21a"/><path d="M21 15H9M14 10l-5 5 5 5" fill="none" stroke="#fff" stroke-width="2"/></svg>
<svg class="arrow-btn" style="left:491px" viewBox="0 0 30 30"><circle cx="15" cy="15" r="15" fill="#e7b000"/><circle cx="15" cy="15" r="12" fill="#f6c21a"/><path d="M9 15h12M16 10l5 5-5 5" fill="none" stroke="#fff" stroke-width="2"/></svg>

<h2 class="featured-title">Featured Project</h2>
<p class="featured-sub">sed do eiusmod</p>
<div class="featured-rule"></div>
<div class="tile" style="left:136px;top:778px;background:linear-gradient(135deg,#8a7560,#c9b9a3 55%,#6b5a48)" role="img" aria-label="Living room interior with stone wall"></div>
<div class="tile is-hover" style="left:278px;top:778px" role="img" aria-label="Balcony scene under a yellow hover overlay">
  <svg width="26" height="26" viewBox="0 0 26 26"><g fill="none" stroke="#fff" stroke-width="3" stroke-linecap="round"><path d="M11 15l4-4"/><path d="M9 12l-3 3a4 4 0 0 0 5.7 5.7l3-3"/><path d="M17 14l3-3a4 4 0 0 0-5.7-5.7l-3 3"/></g></svg>
</div>
<div class="tile" style="left:421px;top:778px;background:linear-gradient(#e6edf3 0%,#efe3b8 45%,#6fa24a 80%)" role="img" aria-label="Cream-coloured house with red roof and lawn"></div>
<div class="tile" style="left:136px;top:875px;background:linear-gradient(135deg,#d2c8b5,#8c7a63 60%,#4a3a2c)" role="img" aria-label="Entrance hall with curved staircase"></div>
<div class="tile" style="left:278px;top:875px;background:linear-gradient(135deg,#e9e4d6,#cfc5ad 55%,#9a8d70)" role="img" aria-label="Bright living room with white sofa"></div>
<div class="tile" style="left:421px;top:875px;background:linear-gradient(#5b9ad8 0%,#c8b89a 45%,#4f8f3a 85%)" role="img" aria-label="Large house with flowering front garden"></div>

<div class="avatar" role="img" aria-label="Portrait of the company CEO"></div>
<p class="quote-name">CEO Lorna Pescott</p>
<p class="quote-lead">Lorem ipsum dolor sit amet consectetur adipiscing elit,</p>
<span class="quote-mark" style="left:134px;top:1066px">&ldquo;</span>
<p class="quote-body">Sed ut perspiciatis unde omnis iste natus error sit voluptatem accusantium doloremque laudantium, totam rem aperiam, eaque ipsa quae ab illo inventore veritatis et quasi architecto beatae vitae dicta sunt explicabo. Nemo enim ipsam voluptatem quia voluptas sit aspernatur aut odit aut fugit, sed quia consequuntur magni dolores eos qui ratione voluptatem sequi nesciunt. Neque porro quisquam est, qui dolorem ipsum quia dolor sit amet, consectetur, adipisci velit, sed quia non numquam eius modi tempora incidunt ut labore et dolore magnam aliquam quaerat voluptatem.</p>
<span class="quote-mark" style="left:530px;top:1112px">&rdquo;</span>

<footer class="site-footer">
  <p class="copyright">Copyright 2014 Venlox - All Rights Reserved - Disclaimer - Terms and Conditions - Privacy Policy</p>
  <div class="social">Social:
    <span class="social-square" aria-label="Social link"></span>
    <span class="social-square" aria-label="Social link"></span>
    <span class="social-square" aria-label="Social link"></span>
    <span class="social-square" aria-label="Social link"></span>
  </div>
</footer>

</body>
</html>
```